The Web Promotion Playbook for Yard & Patio Construction Crews

We need a book cover design that is for a book targeting landscape and outdoor living contractors that helps them grow their business using online marketing.

We run a business focused on this industry so you can see what we do: https://yardcrewgrowthworks.com/

The title is: The Web Promotion Playbook for Yard & Patio Construction Crews

The author is: Trent Varnholm
Some drafts have been done however they're still looking basic and somewhat amateur, we're looking for something that will stand out.

Target Market(s)

Landscape, Hardscape and Outdoor Living Contractors and Business Owners

Industry/Entity Type

Online Marketing

Font styles to use
Serif
Sans Serif

Requirements
Must have
• The part of the title that should stand out the most is the text "Web Promotion Playbook".
Should not have
• The color red

```html
<!DOCTYPE html>
<html lang="en">
<head>
<meta charset="utf-8">
<title>The Web Promotion Playbook for Yard &amp; Patio Construction Crews — Book Cover</title>
<link rel="stylesheet" href="https://fonts.googleapis.com/css2?family=Exo+2:wght@300;400&family=Roboto+Condensed:wght@400;700&display=swap">
<style>
  :root {
    --page-bg: #ffffff;
    --cover-navy: #131f2e;
    --grid-line: rgba(64, 150, 170, 0.16);
    --glow-cyan: #16f0f2;
    --glow-halo: rgba(22, 240, 242, 0.55);
    --title-white: #ffffff;
    --trade-green: #a6f24c;
    --plan-light: #eef6e4;
    --plan-mid: #b8e86a;
    --plan-deep: #6fcf35;
  }

  * { margin: 0; padding: 0; box-sizing: border-box; }

  html, body {
    width: 1200px;
    height: 1000px;
    overflow: hidden;
    background: var(--page-bg);
  }

  .canvas {
    position: relative;
    width: 1200px;
    height: 1000px;
  }

  .book-cover {
    position: absolute;
    left: 300px;
    top: 50px;
    width: 600px;
    height: 900px;
    background-color: var(--cover-navy);
    background-image:
      linear-gradient(to right, var(--grid-line) 1px, transparent 1px),
      linear-gradient(to bottom, var(--grid-line) 1px, transparent 1px);
    background-size: 137px 137px;
    background-position: 0px 46px;
    overflow: hidden;
  }

  .title-block {
    position: absolute;
    left: 0;
    right: 0;
    top: 44px;
    text-align: center;
    line-height: 1;
  }

  .title-line { display: block; }

  .title-small {
    font-family: "Exo 2", sans-serif;
    font-weight: 400;
    font-size: 33px;
    color: var(--title-white);
    letter-spacing: 1px;
  }

  .title-glow {
    font-family: "Exo 2", sans-serif;
    font-weight: 400;
    font-size: 72px;
    color: var(--glow-cyan);
    text-shadow: 0 0 14px var(--glow-halo), 0 0 28px var(--glow-halo);
    letter-spacing: 1px;
    margin-top: -2px;
  }

  .title-plan {
    font-family: "Exo 2", sans-serif;
    font-weight: 300;
    font-size: 58px;
    color: var(--title-white);
    letter-spacing: 5px;
    margin-top: 4px;
  }

  .title-small.for-word { margin-top: 8px; }

  .title-trade {
    font-family: "Roboto Condensed", sans-serif;
    font-weight: 700;
    font-size: 54px;
    color: var(--trade-green);
    margin-top: 8px;
  }

  .title-trade.spaced { letter-spacing: 6px; }

  .title-audience {
    font-family: "Roboto Condensed", sans-serif;
    font-weight: 700;
    font-size: 62px;
    color: var(--title-white);
    letter-spacing: 2px;
    margin-top: 4px;
  }

  .site-plan-strip {
    position: absolute;
    left: 0;
    top: 590px;
    width: 600px;
    height: 330px;
  }

  .author-name {
    position: absolute;
    left: 0;
    right: 0;
    top: 814px;
    text-align: center;
    font-family: "Roboto Condensed", sans-serif;
    font-weight: 400;
    font-size: 40px;
    letter-spacing: 2px;
    color: var(--title-white);
  }
</style>
</head>
<body>
<main class="canvas">
  <section class="book-cover">
    <h1 class="title-block">
      <span class="title-line title-small">THE</span>
      <span class="title-line title-glow">WEB</span>
      <span class="title-line title-glow">PROMOTION</span>
      <span class="title-line title-plan">PLAYBOOK</span>
      <span class="title-line title-small for-word">FOR</span>
      <span class="title-line title-trade spaced">YARD &amp; PATIO</span>
      <span class="title-line title-trade">CONSTRUCTION</span>
      <span class="title-line title-audience">CREWS</span>
    </h1>

    <svg class="site-plan-strip" viewBox="0 0 600 330" role="img" aria-label="Hand-coloured landscape site plan with green trees, a curving path and small buildings, a drafting compass and a pencil in hand, shown on a torn paper strip">
      <defs>
        <linearGradient id="planWash" x1="0" y1="0" x2="1" y2="0.4">
          <stop offset="0" stop-color="var(--plan-light)"/>
          <stop offset="0.3" stop-color="var(--plan-mid)"/>
          <stop offset="0.6" stop-color="var(--plan-deep)"/>
          <stop offset="0.85" stop-color="var(--plan-mid)"/>
          <stop offset="1" stop-color="var(--plan-light)"/>
        </linearGradient>
      </defs>
      <polygon fill="url(#planWash)" points="
        0,8 30,4 62,10 90,2 120,12 150,6 180,14 210,8 240,16 268,10 300,14
        330,8 360,18 390,12 420,20 450,16 480,22 510,18 540,24 570,20 600,16
        600,290 575,300 550,296 525,312 500,308 470,318 440,310 410,318
        380,312 350,318 320,310 290,316 260,308 230,314 200,306 170,312
        140,304 110,310 80,302 50,306 20,300 0,304"/>
    </svg>

    <p class="author-name">Trent Varnholm</p>
  </section>
</main>
</body>
</html>
```